Responsive Rewards Application Design

We are seeking web design for a company rewards application. This application will be used by businesses to drive brand loyalty through a customer rewards program. Administrators of the web application will be able to monitor user activity (sign-up/points/purchases etc), view/create rewards points, and manage promotional campaigns. We are open to all color schemes so long as the design is clean and simple. Also, please provide style ideas for graphical representation of promo stats as well as clean design for our data tables. Attached are the wireframes for our application along with a sample application for reference.

Retail

Coded - Design and coding required

3 page

• Please include responsive design for tablet and mobile views.

```html
<!DOCTYPE html>
<html lang="en">
<head>
<meta charset="utf-8">
<title>Mera Mandi Rewards – Add Campaign</title>
<link href="https://fonts.googleapis.com/css2?family=Open+Sans:wght@400;600;700&display=swap" rel="stylesheet">
<style>
:root{
  --sidebar:#37474f;
  --sidebar-line:#56666d;
  --sidebar-text:#ffffff;
  --accent-yellow:#f3d24b;
  --page-bg:#efefef;
  --card:#ffffff;
  --border:#d6d6d6;
  --text:#3a3a3a;
  --muted:#6b6b6b;
  --purple:#8e3b8a;
  --green:#5ccb1a;
  --dark:#3c4d55;
  --table-head:#e8b866;
  --row-alt:#f1f1f1;
  --edit:#2c8fd6;
  --delete:#d9261c;
}
*{box-sizing:border-box;margin:0;padding:0}
html,body{width:1200px;height:546px;overflow:hidden}
body{font-family:"Open Sans",Arial,sans-serif;color:var(--text);position:relative;background:var(--page-bg)}

.sidebar{position:absolute;left:0;top:0;width:243px;height:546px;background:var(--sidebar);color:var(--sidebar-text)}
.brand{position:absolute;left:28px;top:24px;display:flex;align-items:center}
.brand-mark{width:55px;height:55px;border-radius:50%;background:#e9b54f;border:2px solid #8e3b8a}
.brand-name{margin-left:8px;font-size:21px;line-height:22px;font-weight:400;color:#fff}
.nav{position:absolute;left:27px;top:114px;width:196px;list-style:none}
.nav-item{height:37.5px;display:flex;align-items:center;font-size:10.5px;font-weight:600;letter-spacing:.3px;text-transform:uppercase;border-bottom:1px solid var(--sidebar-line);position:relative}
.nav-item svg{width:10px;height:10px;margin-right:9px;fill:#fff}
.nav-item .chev{position:absolute;right:6px;top:50%;margin-top:-4px;width:7px;height:8px;fill:none;stroke:#fff;stroke-width:1.5;margin-right:0}
.nav-group{border-bottom:1px solid var(--sidebar-line);padding-bottom:8px}
.nav-group .nav-item{border-bottom:none;height:24px}
.subnav{list-style:none;padding-left:26px}
.subnav li{font-size:11px;color:var(--accent-yellow);height:21px;line-height:21px}

.topbar{position:absolute;left:243px;top:0;width:957px;height:95px;background:#fff}
.hamburger{position:absolute;left:22px;top:38px;width:20px;height:17px}
.hamburger span{display:block;height:3px;background:#9a9a9a;margin-bottom:4px}
.search{position:absolute;left:80px;top:33px;width:188px;height:29px;border:1px solid #bdbdbd;border-radius:15px;font-size:10px;color:#777;padding:7px 15px}
.search svg{position:absolute;right:11px;top:8px;width:12px;height:12px}
.user{position:absolute;left:622px;top:30px;display:flex;align-items:center}
.avatar{width:36px;height:36px;border-radius:50%;border:1px solid #cfcfcf;display:flex;align-items:center;justify-content:center}
.user-text{margin-left:14px;line-height:16px}
.user-text .welcome{font-size:12px;font-weight:700;color:var(--purple)}
.user-text .role{font-size:12px;color:var(--muted)}
.account-links{position:absolute;left:770px;top:40px;font-size:12px;color:var(--text)}

.page-title{position:absolute;left:264px;top:118px;font-size:14px;font-weight:700;letter-spacing:.4px;color:#3a4a52}

.form-card{position:absolute;left:266px;top:149px;width:902px;height:117px;background:var(--card)}
.field{position:absolute;top:13px;width:170px}
.field label{display:block;font-size:11px;font-weight:700;color:#333;height:25px}
.field .input{height:29px;border:1px solid var(--border);background:#fff;font-size:10px;padding:7px 9px;position:relative}
.field .input svg{position:absolute;right:9px;top:10px}
.actions{position:absolute;right:15px;top:78px;display:flex;gap:5px}
.btn{width:73px;height:28px;color:#fff;font-size:11px;font-weight:700;display:flex;align-items:center;justify-content:center}
.btn-submit{background:var(--green)}
.btn-cancel{background:var(--purple)}
.btn-next{background:var(--dark)}

.campaign-table{position:absolute;left:266px;top:279px;width:902px;border-collapse:collapse;font-size:10px}
.campaign-table th{background:var(--table-head);color:#fff;font-weight:700;text-align:left;height:37px;padding:0 14px;font-size:11px;border-right:1px solid #f6dcae}
.campaign-table td{height:32.5px;padding:0 14px;color:#444;border-right:1px solid #e3e3e3;background:#fff}
.campaign-table tr:nth-child(even) td{background:var(--row-alt)}
.campaign-table th:last-child,.campaign-table td:last-child{border-right:none}
.icon-cell{text-align:center;padding:0 !important}
.footer-note{position:absolute;left:264px;top:495px;font-size:10px;font-weight:600;color:#333}
</style>
</head>
<body>
<aside class="sidebar">
  <div class="brand">
    <div class="brand-mark"></div>
    <div class="brand-name">Mera Mandi<br>Cash &amp; Carry</div>
  </div>
  <ul class="nav">
    <li class="nav-group">
      <div class="nav-item"><svg viewBox="0 0 10 10"><rect x="0" y="1" width="8" height="8" fill="none" stroke="#fff" stroke-width="1.4"/><path d="M4 6 L9 1" stroke="#fff" stroke-width="1.6"/></svg>Registration<svg class="chev" viewBox="0 0 8 8"><path d="M1 2.5 L4 5.5 L7 2.5"/></svg></div>
      <ul class="subnav"><li>› Store Registration</li><li>› User Registration</li></ul>
    </li>
    <li class="nav-item"><svg viewBox="0 0 10 10"><circle cx="3" cy="3" r="2"/><circle cx="7" cy="3" r="2"/><rect x="0" y="6" width="10" height="4" rx="2"/></svg>Members</li>
    <li class="nav-item"><svg viewBox="0 0 10 10"><rect x="0" y="1" width="10" height="9" fill="none" stroke="#fff" stroke-width="1.4"/><rect x="0" y="1" width="10" height="3"/></svg>Activity</li>
    <li class="nav-item"><svg viewBox="0 0 10 10"><path d="M2 0 H8 V4 A3 3 0 0 1 2 4 Z"/><rect x="4" y="6" width="2" height="2"/><rect x="2.5" y="8" width="5" height="2"/></svg>Rewards<svg class="chev" viewBox="0 0 8 8"><path d="M2.5 1 L5.5 4 L2.5 7"/></svg></li>
    <li class="nav-item"><svg viewBox="0 0 10 10"><path d="M0 3 H3 L9 0 V10 L3 7 H0 Z"/></svg>Campaign<svg class="chev" viewBox="0 0 8 8"><path d="M2.5 1 L5.5 4 L2.5 7"/></svg></li>
    <li class="nav-item"><svg viewBox="0 0 10 10"><rect x="0" y="1" width="8" height="8" fill="none" stroke="#fff" stroke-width="1.4"/><path d="M4 6 L9 1" stroke="#fff" stroke-width="1.6"/></svg>Settings<svg class="chev" viewBox="0 0 8 8"><path d="M2.5 1 L5.5 4 L2.5 7"/></svg></li>
    <li class="nav-item" style="border-bottom:none"><svg viewBox="0 0 10 10"><path d="M0 0 H5 L10 5 L5 10 L0 5 Z"/></svg>Promotions</li>
  </ul>
</aside>

<header class="topbar">
  <div class="hamburger"><span></span><span></span><span></span></div>
  <div class="search">Search..
    <svg viewBox="0 0 12 12"><circle cx="5" cy="5" r="3.8" fill="none" stroke="#777" stroke-width="1.6"/><path d="M8 8 L11 11" stroke="#777" stroke-width="1.8"/></svg>
  </div>
  <div class="user">
    <div class="avatar"><svg width="16" height="18" viewBox="0 0 16 18"><circle cx="8" cy="5" r="4.5" fill="#3c4d55"/><path d="M0 18 V14 A5 5 0 0 1 5 10 H11 A5 5 0 0 1 16 14 V18 Z" fill="#3c4d55"/></svg></div>
    <div class="user-text"><div class="welcome">Welcome</div><div class="role">Super Admin</div></div>
  </div>
  <div class="account-links">Change Password &nbsp;/&nbsp; Sign Out</div>
</header>

<h1 class="page-title">ADD CAMPAIGN</h1>

<section class="form-card">
  <div class="field" style="left:11px"><label>Company/Retailer/Shop</label><div class="input">Select<svg width="6" height="9" viewBox="0 0 6 9"><path d="M0 3.5 L3 0 L6 3.5 Z M0 5.5 L3 9 L6 5.5 Z" fill="#444"/></svg></div></div>
  <div class="field" style="left:188px"><label>Promotinal Name</label><div class="input"></div></div>
  <div class="field" style="left:364px"><label>Promotinal Message</label><div class="input"></div></div>
  <div class="field" style="left:540px"><label>Start Date</label><div class="input"></div></div>
  <div class="field" style="left:716px"><label>End Date</label><div class="input"></div></div>
  <div class="actions">
    <div class="btn btn-submit">Submit</div>
    <div class="btn btn-cancel">Cancel</div>
    <div class="btn btn-next">Next</div>
  </div>
</section>

<table class="campaign-table">
  <colgroup><col style="width:141px"><col style="width:90px"><col style="width:133px"><col style="width:251px"><col style="width:85px"><col style="width:82px"><col style="width:54px"><col style="width:66px"></colgroup>
  <thead><tr><th>Company</th><th>Campaign ID</th><th>Campaign Heading</th><th>Campaign Message</th><th>Start Date</th><th>End Date</th><th>Edit</th><th>Delete</th></tr></thead>
  <tbody>
    <tr><td>Mera Mandi</td><td>1</td><td>Steel WON on Monday</td><td>All Buy Light Products 10% off Until Thursday</td><td>11/04/2016</td><td>11/04/2016</td>
      <td class="icon-cell"><svg width="10" height="10" viewBox="0 0 10 10"><rect x="0.7" y="1.5" width="7.5" height="7.8" fill="none" stroke="#2c8fd6" stroke-width="1.2"/><path d="M4 6 L9.3 0.7" stroke="#2c8fd6" stroke-width="1.6"/></svg></td>
      <td class="icon-cell"><svg width="9" height="10" viewBox="0 0 9 10"><rect x="0" y="1" width="9" height="2" fill="#d9261c"/><path d="M1 3.5 H8 L7 10 H2 Z" fill="#d9261c"/></svg></td></tr>
    <tr><td>Mera Mandi</td><td>4</td><td>Double Points</td><td>Earn Double Point on your Next Purchase</td><td>11/04/2016</td><td>11/04/2016</td>
      <td class="icon-cell"><svg width="10" height="10" viewBox="0 0 10 10"><rect x="0.7" y="1.5" width="7.5" height="7.8" fill="none" stroke="#2c8fd6" stroke-width="1.2"/><path d="M4 6 L9.3 0.7" stroke="#2c8fd6" stroke-width="1.6"/></svg></td>
      <td class="icon-cell"><svg width="9" height="10" viewBox="0 0 9 10"><rect x="0" y="1" width="9" height="2" fill="#d9261c"/><path d="M1 3.5 H8 L7 10 H2 Z" fill="#d9261c"/></svg></td></tr>
    <tr><td>Rebound Arcade Cafe</td><td>2</td><td>Spot Discount</td><td>$3 off Your Next $30 Purchase</td><td>11/04/2016</td><td>11/04/2016</td>
      <td class="icon-cell"><svg width="10" height="10" viewBox="0 0 10 10"><rect x="0.7" y="1.5" width="7.5" height="7.8" fill="none" stroke="#2c8fd6" stroke-width="1.2"/><path d="M4 6 L9.3 0.7" stroke="#2c8fd6" stroke-width="1.6"/></svg></td>
      <td class="icon-cell"><svg width="9" height="10" viewBox="0 0 9 10"><rect x="0" y="1" width="9" height="2" fill="#d9261c"/><path d="M1 3.5 H8 L7 10 H2 Z" fill="#d9261c"/></svg></td></tr>
    <tr><td>Grand Cellar Spirits</td><td>5</td><td>Double Points</td><td>$3 off Your Next $30 Purchase</td><td>11/04/2016</td><td>11/04/2016</td>
      <td class="icon-cell"><svg width="10" height="10" viewBox="0 0 10 10"><rect x="0.7" y="1.5" width="7.5" height="7.8" fill="none" stroke="#2c8fd6" stroke-width="1.2"/><path d="M4 6 L9.3 0.7" stroke="#2c8fd6" stroke-width="1.6"/></svg></td>
      <td class="icon-cell"><svg width="9" height="10" viewBox="0 0 9 10"><rect x="0" y="1" width="9" height="2" fill="#d9261c"/><path d="M1 3.5 H8 L7 10 H2 Z" fill="#d9261c"/></svg></td></tr>
    <tr><td>Grand Cellar Spirits</td><td>3</td><td>Diwali &nbsp;Bumper</td><td>$3 off Your Next $30 Purchase</td><td>11/04/2016</td><td>11/04/2016</td>
      <td class="icon-cell"><svg width="10" height="10" viewBox="0 0 10 10"><rect x="0.7" y="1.5" width="7.5" height="7.8" fill="none" stroke="#2c8fd6" stroke-width="1.2"/><path d="M4 6 L9.3 0.7" stroke="#2c8fd6" stroke-width="1.6"/></svg></td>
      <td class="icon-cell"><svg width="9" height="10" viewBox="0 0 9 10"><rect x="0" y="1" width="9" height="2" fill="#d9261c"/><path d="M1 3.5 H8 L7 10 H2 Z" fill="#d9261c"/></svg></td></tr>
  </tbody>
</table>

<p class="footer-note">Everyone come and see how good &nbsp;I Luck !</p>
</body>
</html>
```